Meadowrun Honey labels

I have honey farm . I would like to sale it at grocery stores. I need really unique and very attractive designed labels, I would like to see writings 100% Natural honey and GMO free ,. Company name "MeadowrunHoney" . I want to put 2 labels and one ribbon tag in middle and round label on top of lid(only one diamond shape in the middle).I would like to see bee flying over red flower and at the left side flower field and right side bee putting honey into honey hives. I have attached example pictures of Honey Jars labels, tags and type. I have two different type of Honey jars i have also attached picture of those jars. For jar with red lid. If middle label little bit bigger than measurement thats ok because writing has to fit.

Target Market(s)

Grocery stores

Industry/Entity Type

Farm

Requirements
Must have
• 100% Natural Honey, GMO Free, Company name Meadowrun Honey, attractive and unique design. bee flying over flower, right side label flower field left side bee putting honey into bee hives.

```html
<!DOCTYPE html>
<html lang="en">
<head>
<meta charset="utf-8">
<title>Meadowrun Honey – Jar Label Set</title>
<link rel="stylesheet" href="https://fonts.googleapis.com/css2?family=Playfair+Display:wght@700&family=Cormorant+Garamond:wght@500;600&display=swap">
<style>
  :root {
    --label-red: #8f1b20;
    --label-red-deep: #6e1216;
    --honey-gold: #f4b51e;
    --cream: #f4e7d2;
    --backdrop: #ece9e4;
  }
  html, body {
    margin: 0;
    padding: 0;
    width: 840px;
    height: 1200px;
    overflow: hidden;
    background: var(--backdrop);
  }
  .label-sheet { display: block; width: 840px; height: 1200px; }
  .label-base { fill: var(--label-red); }
  .label-shade { fill: var(--label-red-deep); }
  .hairline { fill: none; stroke: var(--cream); stroke-width: 1.2; stroke-dasharray: 2 4; opacity: .7; }
  .brand-name {
    font-family: "Playfair Display", serif;
    font-weight: 700;
    fill: var(--honey-gold);
  }
  .claim {
    font-family: "Cormorant Garamond", serif;
    font-weight: 600;
    fill: var(--cream);
    letter-spacing: .5px;
  }
  .body-copy {
    font-family: "Cormorant Garamond", serif;
    font-weight: 500;
    fill: var(--cream);
  }
  .emblem-ring { fill: none; stroke: var(--honey-gold); stroke-width: 1.6; }
  .art-slot { fill: var(--honey-gold); opacity: .85; }
</style>
</head>
<body>
<svg class="label-sheet" viewBox="0 0 840 1200" xmlns="http://www.w3.org/2000/svg">

  <g class="lid-label">
    <circle class="label-shade" cx="420" cy="210" r="170"/>
    <circle class="label-base" cx="420" cy="210" r="160"/>
    <circle class="hairline" cx="420" cy="210" r="148"/>
    <text class="brand-name" x="420" y="182" font-size="28" text-anchor="middle">Meadowrun Honey</text>
    <text class="claim" x="420" y="224" font-size="22" text-anchor="middle">100% NATURAL HONEY</text>
    <text class="claim" x="420" y="252" font-size="22" text-anchor="middle">GMO FREE</text>
    <text class="body-copy" x="420" y="284" font-size="16" text-anchor="middle">net weight: 250g</text>
  </g>

  <g class="ribbon-tag">
    <rect class="label-shade" x="392" y="400" width="56" height="260"/>
    <rect class="label-base" x="396" y="400" width="48" height="260"/>
    <circle class="emblem-ring" cx="420" cy="500" r="15"/>
    <circle class="art-slot" cx="420" cy="500" r="6"/>
  </g>

  <g class="wrap-band">
    <rect class="label-base" x="60" y="660" width="720" height="230"/>
    <rect class="hairline" x="70" y="670" width="700" height="210"/>

    <g class="side-label side-label--left">
      <text class="brand-name" x="168" y="725" font-size="20" text-anchor="middle">Meadowrun Honey</text>
      <text class="body-copy" font-size="13" text-anchor="middle">
        <tspan x="168" y="765">Gathered from wildflower meadows</tspan>
        <tspan x="168" y="784">and gently strained to keep every</tspan>
        <tspan x="168" y="803">drop pure, raw and full of</tspan>
        <tspan x="168" y="822">natural flavour.</tspan>
      </text>
    </g>

    <g class="side-label side-label--right">
      <text class="brand-name" x="672" y="725" font-size="20" text-anchor="middle">Meadowrun Honey</text>
      <text class="body-copy" font-size="13" text-anchor="middle">
        <tspan x="672" y="765">Enjoy by the spoonful, stir into tea</tspan>
        <tspan x="672" y="784">or drizzle over warm bread. Store</tspan>
        <tspan x="672" y="803">at room temperature away</tspan>
        <tspan x="672" y="822">from sunlight.</tspan>
      </text>
    </g>
  </g>

  <g class="front-label">
    <polygon class="label-shade" points="420,584 576,668 576,872 420,956 264,872 264,668"/>
    <polygon class="label-base" points="420,594 568,674 568,866 420,946 272,866 272,674"/>
    <polygon class="hairline" points="420,610 554,682 554,858 420,930 286,858 286,682"/>
    <text class="brand-name" x="420" y="738" font-size="34" text-anchor="middle">Meadowrun</text>
    <text class="brand-name" x="420" y="778" font-size="34" text-anchor="middle">Honey</text>
    <rect class="art-slot" x="494" y="752" width="12" height="32" rx="6" role="img" aria-label="Honey dipper with a golden drip"/>
    <circle class="emblem-ring" cx="420" cy="808" r="20"/>
    <text class="claim" x="420" y="813" font-size="13" text-anchor="middle">100%</text>
    <text class="claim" x="420" y="850" font-size="21" text-anchor="middle">NATURAL HONEY</text>
    <text class="claim" x="420" y="874" font-size="21" text-anchor="middle">GMO FREE</text>
    <text class="body-copy" x="420" y="898" font-size="12" text-anchor="middle">Net weight | 250g</text>
  </g>

</svg>
</body>
</html>
```